Scheduled Servicing Forms

Corvella Systems requires two schedule servicing forms to be created on designer templates for our engineers to complete when servicing customers. We will complete these forms on a periodic basis, and send to the customer on completion of the work.
We have two forms that need to be created:
• Hybrid Cloud Customer Service
• Veltrix Cloud Customer Service
Please do not reference our website for ideas as its about to change. “Specialised Consulting” is our new go to market, not “Pushing the Boundaries of Technology. Our new website (still under development) is available at https://corvellasystems.qzt.net.au and will be officially launched shortly.
Our company theme is “Blue” and we want to keep a blue theme for the work.
Please ensure there is “Ample” space for engineers to write comments next to each audit item.
We have uploaded examples of the content that needs to be created for both form in Word and Excel format.
The designer must upload the source files (not just PDF) so we can edit the content on the forms at a later date.
The forms must be in standard A4 size (multiple pages).
Industry/Entity Type
Information Technology
Look and feel

```html
<!DOCTYPE html>
<html lang="en">
<head>
<meta charset="utf-8">
<title>Corvella Systems – Scheduled Service Checklists</title>
<link rel="stylesheet" href="https://fonts.googleapis.com/css2?family=Open+Sans:wght@400;600;700&display=swap">
<style>
:root{
  --bg-top:#1c1c1c;
  --bg-bottom:#2b2b2b;
  --navy:#262a72;
  --navy-deep:#1d2160;
  --blue:#1f6fc4;
  --blue-light:#2d92dd;
  --title-blue:#1a7fd3;
  --ink:#333;
  --rule:#666;
  --muted:#6a6a6a;
  --wm:#000;
  --red:#d9232b;
  --dblue:#1d74d0;
  --green:#3db54a;
  --orange:#f7941d;
}
*{box-sizing:border-box;margin:0;padding:0}
html,body{width:1200px;height:2230px;overflow:hidden}
body{background:linear-gradient(180deg,var(--bg-top),var(--bg-bottom) 45%,var(--bg-top));font-family:"Open Sans",Arial,sans-serif;position:relative}
.section-title{position:absolute;left:33px;font-size:15px;font-weight:700;color:var(--title-blue);letter-spacing:.1px}
.page{position:absolute;width:360px;height:507px;background:#fff;overflow:hidden}
.strip-l{position:absolute;left:0;top:60px;width:16px;height:404px;background:var(--navy)}
.strip-r{position:absolute;right:0;top:39px;width:16px;height:425px;background:linear-gradient(180deg,#1e5cae,var(--blue-light) 60%,#1e5cae)}
.slash{position:absolute;left:0;top:0}
.foot-line{position:absolute;left:0;top:493px;width:190px;height:2px;background:linear-gradient(90deg,#eee,#9a9a9a)}
.foot-url{position:absolute;left:198px;top:488px;font-size:6.3px;color:#555}
.foot-div{position:absolute;left:316px;top:487px;width:.8px;height:10px;background:#999}
.foot-num{position:absolute;left:332px;top:488px;font-size:6.3px;color:#555}
.foot-bar{position:absolute;left:0;bottom:0;width:100%;height:2px;background:var(--navy)}
.mark{position:absolute;left:0;width:100%;text-align:center;color:var(--wm);opacity:.05;font-weight:700;pointer-events:none}
.mark.name{top:300px;font-size:20px;letter-spacing:1px}
.mark.tag{top:330px;font-size:12px;letter-spacing:1px}
/* cover */
.brand{position:absolute;left:22px;top:22px;display:flex;align-items:center;gap:6px}
.brand i{width:14px;height:14px;background:var(--navy)}
.brand span{font-size:10px;font-weight:700;color:var(--navy);letter-spacing:.6px}
.doc-title{position:absolute;right:16px;top:19px;font-size:6.8px;font-weight:700;color:#222;letter-spacing:.2px}
.ribbon{position:absolute;left:0;top:0}
.ribbon-text{position:absolute;right:16px;top:40px;font-size:8.3px;color:#fff}
.cover-band{position:absolute;left:0;top:57px;width:100%;height:411px;background:linear-gradient(90deg,var(--navy) 0%,var(--navy) 8%,#253f96 45%,var(--blue) 85%,var(--blue-light))}
.card{position:absolute;left:16px;top:73px;width:328px;height:395px;background:#fff}
.meta{position:absolute;left:24px;font-size:6px;color:#333;display:flex}
.meta dt{width:60px}
.checklist{position:absolute;left:24px;top:124px;width:311px;border:1px solid var(--rule);background:#fff}
.sheet .checklist{left:26px;top:26px;width:309px}
.head{display:grid;grid-template-columns:130px 1fr;height:12px;background:var(--navy-deep);color:#fff;font-size:5.8px;font-weight:700;text-align:center;line-height:12px}
.head span:first-child{border-right:1px solid #fff}
.row{display:grid;grid-template-columns:130px 1fr;height:36px;border-top:1px solid var(--rule)}
.checklist>.row:first-child{border-top:0}
.item{padding:3px 3px;font-size:5.5px;line-height:1.32;color:var(--ink);border-right:1px solid var(--rule)}
.res{padding:3px 3px;font-size:5.3px;line-height:1.35;color:var(--ink)}
.yn{display:flex;align-items:center}
.yn i{display:inline-block;width:7px;height:6px;border:.8px solid #444;margin-right:3px}
.yn i+i{margin-left:24px}
.ln{display:block;width:150px;border-bottom:.7px solid #555;margin-top:8px}
.recs{list-style:none;margin:1px 0 0 10px}
.recs li{display:flex;gap:4px;height:6.5px;line-height:6.5px}
.recs li b{flex:0 0 140px;border-bottom:.6px solid #555}
.sign{position:absolute;left:24px;font-size:6px;color:#333;display:flex}
.sign dt{width:50px}
/* delivery */
.delivery-title{position:absolute;left:521px;top:1866px;font-size:17px;color:#fff}
.files{position:absolute;left:521px;top:1899px;display:flex;gap:12px}
.file{position:relative;width:94px;height:115px}
.file span{position:absolute;left:0;width:100%;top:68px;text-align:center;font-size:21px;color:#fff}
</style>
</head>
<body>

<h2 class="section-title" style="top:30px">Hybrid Cloud Customer Service</h2>

<!-- Hybrid page 1 -->
<section class="page cover" style="left:35px;top:68px">
  <svg class="ribbon" width="360" height="60" aria-hidden="true">
    <defs><linearGradient id="rb1" x1="0" x2="1"><stop offset="0" stop-color="#1b3f94"/><stop offset="1" stop-color="#2b8ad8"/></linearGradient></defs>
    <polygon points="330,0 360,0 360,-2 " fill="#bbb"/>
    <line x1="326" y1="16" x2="360" y2="-2" stroke="#b5b5b5" stroke-width="4"/>
    <polygon points="176,53 196,37 360,37 360,53" fill="url(#rb1)"/>
    <line x1="172" y1="56" x2="360" y2="56" stroke="#c9c9c9" stroke-width="1"/>
  </svg>
  <div class="brand"><i></i><span>CORVELLA SYSTEMS</span></div>
  <div class="doc-title">SCHEDULED SERVICE CHECKLIST</div>
  <div class="ribbon-text">Veltrix Hybrid/On-Premise</div>
  <div class="cover-band"></div>
  <div class="card"></div>
  <dl class="meta" style="top:80px"><dt>Customer</dt><dd>: ________________________________________________________</dd></dl>
  <dl class="meta" style="top:94px"><dt>Date</dt><dd>: _____/_____/_____</dd></dl>
  <div class="checklist">
    <div class="head"><span>Maintenance Check</span><span>Result</span></div>
    <div class="row"><div class="item">Active backup for all 365 accounts (manual check) - ensuring all items are included in the job</div><div class="res"><p class="yn"><i></i>YES<i></i>NO</p><p>Comment:</p><b class="ln"></b></div></div>
    <div class="row"><div class="item">Test restore from server backup</div><div class="res"><p class="yn"><i></i>YES<i></i>NO</p><p>Comment:</p><b class="ln"></b></div></div>
    <div class="row"><div class="item">Test restore of an email</div><div class="res"><p class="yn"><i></i>YES<i></i>NO</p><p>Comment:</p><b class="ln"></b></div></div>
    <div class="row"><div class="item">Test restore of ShareSpace file</div><div class="res"><p class="yn"><i></i>YES<i></i>NO</p><p>Comment:</p><b class="ln"></b></div></div>
    <div class="row"><div class="item">Log into Antivirus products (ensure all endpoint devices have active antivirus and are up to date)</div><div class="res"><p class="yn"><i></i>YES<i></i>NO</p><p>Comment:</p><b class="ln"></b></div></div>
    <div class="row"><div class="item">Check Spam filters</div><div class="res"><p class="yn"><i></i>YES<i></i>NO</p><p>Comment:</p><b class="ln"></b></div></div>
    <div class="row"><div class="item">Check that all users have MFA enabled</div><div class="res"><p class="yn"><i></i>YES<i></i>NO</p><p>Comment:</p><b class="ln"></b></div></div>
    <div class="row"><div class="item">Review VX365 Risk Detections</div><div class="res"><p class="yn"><i></i>YES<i></i>NO</p><p>Comment:</p><b class="ln"></b></div></div>
    <div class="row"><div class="item">Confirm Audit Log enabled</div><div class="res"><p class="yn"><i></i>YES<i></i>NO</p><p>Comment:</p><b class="ln"></b></div></div>
  </div>
  <div class="mark name">CORVELLA SYSTEMS</div><div class="mark tag">SPECIALISED CONSULTING</div>
  <div class="foot-line"></div><div class="foot-url">corvellasystems.qzt.net.au</div><div class="foot-div"></div><div class="foot-num">1</div><div class="foot-bar"></div>
</section>

<!-- Hybrid page 2 -->
<section class="page sheet" style="left:411px;top:68px">
  <svg class="slash" width="50" height="20" aria-hidden="true"><line x1="-2" y1="17" x2="36" y2="-1" stroke="#b5b5b5" stroke-width="4"/></svg>
  <div class="strip-l"></div><div class="strip-r"></div>
  <div class="checklist">
    <div class="row"><div class="item">Review VX365 license expiry dates</div><div class="res"><p>Expiry Date: _________________</p><p>Comment:</p><b class="ln"></b></div></div>
    <div class="row"><div class="item">Review external sharing in ShareSpace/CloudDrive</div><div class="res"><p class="yn"><i></i>YES<i></i>NO</p><p>Comment:</p><b class="ln"></b></div></div>
    <div class="row"><div class="item">Check Compliance status</div><div class="res"><p class="yn"><i></i>YES<i></i>NO</p><p>Comment:</p><b class="ln"></b></div></div>
    <div class="row" style="height:94px"><div class="item">Check and record Veltrix security score</div><div class="res"><p class="yn"><i></i>YES<i></i>NO</p><p>Score: ______________</p><p>Top 5 Recommendations:</p><ol class="recs"><li>1.<b></b></li><li>2.<b></b></li><li>3.<b></b></li><li>4.<b></b></li><li>5.<b></b></li></ol><p style="margin-top:5px">Comment:</p><b class="ln"></b></div></div>
    <div class="row"><div class="item">Conditional access Rules (no silly Rules, Geolocation filters in place for Sanctioned Countries)</div><div class="res"><p class="yn"><i></i>YES<i></i>NO</p><p>Comment:</p><b class="ln"></b></div></div>
    <div class="row"><div class="item">Review security access of all privileged access accounts</div><div class="res"><p class="yn"><i></i>YES<i></i>NO</p><p>Comment:</p><b class="ln"></b></div></div>
    <div class="row"><div class="item">Review Application Patching and confirm all workstations &amp; servers are up to date</div><div class="res"><p class="yn"><i></i>YES<i></i>NO</p><p>Comment:</p><b class="ln"></b></div></div>
    <div class="row"><div class="item">Review Velos Patching and confirm all workstations &amp; servers are up to date</div><div class="res"><p class="yn"><i></i>YES<i></i>NO</p><p>Comment:</p><b class="ln"></b></div></div>
    <div class="row"><div class="item">Review domain expiry dates</div><div class="res"><p>Expiry Date: _____/_____/_____</p><p>Comment:</p><b class="ln"></b></div></div>
    <div class="row"><div class="item">Review certificate expiry dates (including internal services i.e. HyperCenter)</div><div class="res"><p>Expiry Date: _____/_____/_____</p><p>Comment:</p><b class="ln"></b></div></div>
    <div class="row"><div class="item">Confirm all devices are in Application Whitelisting enforcement mode</div><div class="res"><p class="yn"><i></i>YES<i></i>NO</p><p>Comment:</p><b class="ln"></b></div></div>
  </div>
  <div class="mark name">CORVELLA SYSTEMS</div><div class="mark tag">SPECIALISED CONSULTING</div>
  <div class="foot-line"></div><div class="foot-url">corvellasystems.qzt.net.au</div><div class="foot-div"></div><div class="foot-num">2</div><div class="foot-bar"></div>
</section>

<!-- Hybrid page 3 -->
<section class="page sheet" style="left:789px;top:68px">
  <svg class="slash" width="50" height="20" aria-hidden="true"><line x1="-2" y1="17" x2="36" y2="-1" stroke="#b5b5b5" stroke-width="4"/></svg>
  <div class="strip-l"></div><div class="strip-r"></div>
  <div class="checklist">
    <div class="row"><div class="item">Ensure DMARC, DKIM and SPF records are in place and up to date</div><div class="res"><p class="yn"><i></i>YES<i></i>NO</p><p>Comment:</p><b class="ln"></b></div></div>
    <div class="row"><div class="item">Confirm Retention Policies is configured and time specified</div><div class="res"><p class="yn"><i></i>YES<i></i>NO</p><p>Comment:</p><b class="ln"></b></div></div>
    <div class="row"><div class="item">Review Network Firewall Firmware is up to date and no ANY &lt;&gt; ANY rules in place</div><div class="res"><p class="yn"><i></i>YES<i></i>NO</p><p>Comment:</p><b class="ln"></b></div></div>
    <div class="row"><div class="item">Ensure critical network equipment is connected to UPS (min 20min run time)</div><div class="res"><p class="yn"><i></i>YES<i></i>NO</p><p>Comment:</p><b class="ln"></b></div></div>
    <div class="row"><div class="item">Ensure Access Layer Network device firmware is up to date (Switches &amp; Access Points)</div><div class="res"><p class="yn"><i></i>YES<i></i>NO</p><p>Comment:</p><b class="ln"></b></div></div>
    <div class="row"><div class="item">Ensure the latest backup configuration for managed network devices is current or automatically backed up monthly. Saved Network location must be secured</div><div class="res"><p class="yn"><i></i>YES<i></i>NO</p><p>Comment:</p><b class="ln"></b></div></div>
    <div class="row"><div class="item">Ensure MFP's &amp; Printers drivers up to date. No Print Nightmare</div><div class="res"><p class="yn"><i></i>YES<i></i>NO</p><p>Comment:</p><b class="ln"></b></div></div>
    <div class="row"><div class="item">NAC Certificates are current (PEAP/EAP-TLS)</div><div class="res"><p class="yn"><i></i>YES<i></i>NO</p><p>Comment:</p><b class="ln"></b></div></div>
    <div class="row"><div class="item">Check DLP alerts and configuration</div><div class="res"><p class="yn"><i></i>YES<i></i>NO</p><p>Comment:</p><b class="ln"></b></div></div>
    <div class="row"><div class="item">Review &amp; address SIEM and SOC alerts</div><div class="res"><p class="yn"><i></i>YES<i></i>NO</p><p>Comment:</p><b class="ln"></b></div></div>
    <div class="row"><div class="item">Email alerting on firewall changes sent to <u style="color:#1d5fc4">alerts@crvl.net.au</u></div><div class="res"><p class="yn"><i></i>YES<i></i>NO</p><p>Comment:</p><b class="ln"></b></div></div>
    <div class="row"><div class="item">Review Vulnerability Scan reports; Remediate as required</div><div class="res"><p class="yn"><i></i>YES<i></i>NO</p><p>Comment:</p><b class="ln"></b></div></div>
  </div>
  <div class="mark name">CORVELLA SYSTEMS</div><div class="mark tag">SPECIALISED CONSULTING</div>
  <div class="foot-line"></div><div class="foot-url">corvellasystems.qzt.net.au</div><div class="foot-div"></div><div class="foot-num">3</div><div class="foot-bar"></div>
</section>

<!-- Hybrid page 4 -->
<section class="page sheet" style="left:35px;top:594px">
  <svg class="slash" width="50" height="20" aria-hidden="true"><line x1="-2" y1="17" x2="36" y2="-1" stroke="#b5b5b5" stroke-width="4"/></svg>
  <div class="strip-l"></div><div class="strip-r"></div>
  <div class="checklist" style="top:27px">
    <div class="row"><div class="item">Confirm all Infrastructure is in Monitoring</div><div class="res"><p class="yn"><i></i>YES<i></i>NO</p><p>Comment:</p><b class="ln"></b></div></div>
    <div class="row"><div class="item">Check vendor Maintenance period of all infrastructure</div><div class="res"><p class="yn"><i></i>YES<i></i>NO</p><p>Comment:</p><b class="ln"></b></div></div>
    <div class="row"><div class="item">Check time sync across all/critical devices</div><div class="res"><p class="yn"><i></i>YES<i></i>NO</p><p>Comment:</p><b class="ln"></b></div></div>
    <div class="row"><div class="item">Check infrastructure firmware</div><div class="res"><p class="yn"><i></i>YES<i></i>NO</p><p>Comment:</p><b class="ln"></b></div></div>
    <div class="row"><div class="item">Review monitoring logs/portal for active alerts</div><div class="res"><p class="yn"><i></i>YES<i></i>NO</p><p>Comment:</p><b class="ln"></b></div></div>
    <div class="row"><div class="item">Review event logs on critical servers</div><div class="res"><p class="yn"><i></i>YES<i></i>NO</p><p>Comment:</p><b class="ln"></b></div></div>
    <div class="row"><div class="item">Check Backups both local and airgap</div><div class="res"><p class="yn"><i></i>YES<i></i>NO</p><p>Comment:</p><b class="ln"></b></div></div>
    <div class="row"><div class="item">Check transaction logs purged by backup</div><div class="res"><p class="yn"><i></i>YES<i></i>NO</p><p>Comment:</p><b class="ln"></b></div></div>
    <div class="row"><div class="item">Check IdentityHub sync</div><div class="res"><p class="yn"><i></i>YES<i></i>NO</p><p>Comment:</p><b class="ln"></b></div></div>
    <div class="row"><div class="item">Check that application proxies are up to date</div><div class="res"><p>Expiry Date: ____/____/____</p><p>Comment:</p><b class="ln"></b></div></div>
    <div class="row"><div class="item">Service Accounts are used where possible</div><div class="res"><p class="yn"><i></i>YES<i></i>NO</p><p>Comment:</p><b class="ln"></b></div></div>
    <div class="row" style="height:58px"><div class="item">Check Domain Admin, Enterprise Admin, Record Membership and last login timestamps</div><div class="res"><p class="yn"><i></i>YES<i></i>NO</p><p style="margin-top:6px">Comment:</p><b class="ln"></b><ol class="recs" style="margin-top:6px"><li>1.<b style="flex-basis:150px"></b></li><li>2.<b style="flex-basis:150px"></b></li></ol></div></div>
  </div>
  <div class="mark name">CORVELLA SYSTEMS</div><div class="mark tag">SPECIALISED CONSULTING</div>
  <div class="foot-line"></div><div class="foot-url">corvellasystems.qzt.net.au</div><div class="foot-div"></div><div class="foot-num">4</div><div class="foot-bar"></div>
</section>

<!-- Hybrid page 5 -->
<section class="page sheet" style="left:411px;top:594px">
  <svg class="slash" width="50" height="20" aria-hidden="true"><line x1="-2" y1="17" x2="36" y2="-1" stroke="#b5b5b5" stroke-width="4"/></svg>
  <div class="strip-l"></div><div class="strip-r"></div>
  <div class="checklist" style="top:27px">
    <div class="row" style="height:35px"><div class="item"></div><div class="res"><ol class="recs"><li>3.<b style="flex-basis:150px"></b></li><li>4.<b style="flex-basis:150px"></b></li><li>5.<b style="flex-basis:150px"></b></li></ol></div></div>
    <div class="row"><div class="item">Check DR replication</div><div class="res"><p class="yn"><i></i>YES<i></i>NO</p><p>Comment:</p><b class="ln"></b></div></div>
    <div class="row"><div class="item">Check email alerts are configured in IPMI/ServerGuard etc.</div><div class="res"><p class="yn"><i></i>YES<i></i>NO</p><p>Comment:</p><b class="ln"></b></div></div>
    <div class="row"><div class="item">Check disk space remaining on servers and SAN block storage volumes</div><div class="res"><p class="yn"><i></i>YES<i></i>NO</p><p>Comment:</p><b class="ln"></b></div></div>
    <div class="row"><div class="item">Review scheduled tasks on servers</div><div class="res"><p class="yn"><i></i>YES<i></i>NO</p><p>Comment:</p><b class="ln"></b></div></div>
    <div class="row"><div class="item">Check EUC applications are not installed on servers</div><div class="res"><p class="yn"><i></i>YES<i></i>NO</p><p>Comment:</p><b class="ln"></b></div></div>
    <div class="row"><div class="item">Server Start-up and Shutdown Sequence configured in Hypervisors</div><div class="res"><p class="yn"><i></i>YES<i></i>NO</p><p>Comment:</p><b class="ln"></b></div></div>
    <div class="row"><div class="item">Review NodeCtl/RackCtl Auto-Start after power loss</div><div class="res"><p class="yn"><i></i>YES<i></i>NO</p><p>Comment:</p><b class="ln"></b></div></div>
    <div class="row"><div class="item">Onsite Visit (Check rack is neat, tidy and locked)</div><div class="res"><p class="yn"><i></i>YES<i></i>NO</p><p>Comment:</p><b class="ln"></b></div></div>
  </div>
  <dl class="sign" style="top:366px"><dt>Completed By</dt><dd>: ______________________________</dd></dl>
  <dl class="sign" style="top:381px"><dt>Signature</dt><dd>: ______________________________</dd></dl>
  <dl class="sign" style="top:396px"><dt>Date</dt><dd>: ______________________________</dd></dl>
  <div class="mark name">CORVELLA SYSTEMS</div><div class="mark tag">SPECIALISED CONSULTING</div>
  <div class="foot-line"></div><div class="foot-url">corvellasystems.qzt.net.au</div><div class="foot-div"></div><div class="foot-num">5</div><div class="foot-bar"></div>
</section>

<h2 class="section-title" style="top:1123px">Veltrix Cloud Customer Service</h2>

<!-- Cloud page 1 -->
<section class="page cover" style="left:35px;top:1161px">
  <svg class="ribbon" width="360" height="60" aria-hidden="true">
    <defs><linearGradient id="rb2" x1="0" x2="1"><stop offset="0" stop-color="#1b3f94"/><stop offset="1" stop-color="#2b8ad8"/></linearGradient></defs>
    <line x1="326" y1="16" x2="360" y2="-2" stroke="#b5b5b5" stroke-width="4"/>
    <polygon points="176,53 196,37 360,37 360,53" fill="url(#rb2)"/>
    <line x1="172" y1="56" x2="360" y2="56" stroke="#c9c9c9" stroke-width="1"/>
  </svg>
  <div class="brand"><i></i><span>CORVELLA SYSTEMS</span></div>
  <div class="doc-title">SCHEDULED SERVICE CHECKLIST</div>
  <div class="ribbon-text">Veltrix Cloud Customer</div>
  <div class="cover-band"></div>
  <div class="card"></div>
  <dl class="meta" style="top:80px"><dt>Customer</dt><dd>: ________________________________________________________</dd></dl>
  <dl class="meta" style="top:94px"><dt>Date</dt><dd>: _____/_____/_____</dd></dl>
  <div class="checklist">
    <div class="head"><span>Maintenance Check</span><span>Result</span></div>
    <div class="row"><div class="item">Active Backup for all 365 accounts (manual check) - ensuring all items are included in the job</div><div class="res"><p class="yn"><i></i>YES<i></i>NO</p><p>Comment:</p><b class="ln"></b></div></div>
    <div class="row"><div class="item">Test restore of an email</div><div class="res"><p class="yn"><i></i>YES<i></i>NO</p><p>Comment:</p><b class="ln"></b></div></div>
    <div class="row"><div class="item">Test restore of ShareSpace file</div><div class="res"><p class="yn"><i></i>YES<i></i>NO</p><p>Comment:</p><b class="ln"></b></div></div>
    <div class="row"><div class="item">Log into Antivirus products (ensure all endpoint devices have active antivirus and are up to date)</div><div class="res"><p class="yn"><i></i>YES<i></i>NO</p><p>Comment:</p><b class="ln"></b></div></div>
    <div class="row"><div class="item">Check Spam Filters</div><div class="res"><p class="yn"><i></i>YES<i></i>NO</p><p>Comment:</p><b class="ln"></b></div></div>
    <div class="row"><div class="item">Check that all users have MFA enabled</div><div class="res"><p class="yn"><i></i>YES<i></i>NO</p><p>Comment:</p><b class="ln"></b></div></div>
    <div class="row"><div class="item">Review VX365 Risk Detections (User and Device Logins)</div><div class="res"><p class="yn"><i></i>YES<i></i>NO</p><p>Comment:</p><b class="ln"></b></div></div>
    <div class="row"><div class="item">Confirm Audit Logging enabled</div><div class="res"><p class="yn"><i></i>YES<i></i>NO</p><p>Comment:</p><b class="ln"></b></div></div>
    <div class="row"><div class="item">Review VX365 license expiry dates</div><div class="res"><p>Expiry Date: _________________</p><p>Comment:</p><b class="ln"></b></div></div>
  </div>
  <div class="mark name">CORVELLA SYSTEMS</div><div class="mark tag">SPECIALISED CONSULTING</div>
  <div class="foot-line"></div><div class="foot-url">corvellasystems.qzt.net.au</div><div class="foot-div"></div><div class="foot-num">1</div><div class="foot-bar"></div>
</section>

<!-- Cloud page 2 -->
<section class="page sheet" style="left:411px;top:1161px">
  <svg class="slash" width="50" height="20" aria-hidden="true"><line x1="-2" y1="17" x2="36" y2="-1" stroke="#b5b5b5" stroke-width="4"/></svg>
  <div class="strip-l"></div><div class="strip-r"></div>
  <div class="checklist">
    <div class="row"><div class="item">Review external sharing in ShareSpace/CloudDrive</div><div class="res"><p class="yn"><i></i>YES<i></i>NO</p><p>Comment:</p><b class="ln"></b></div></div>
    <div class="row"><div class="item">Check Compliance status</div><div class="res"><p class="yn"><i></i>YES<i></i>NO</p><p>Comment:</p><b class="ln"></b></div></div>
    <div class="row" style="height:94px"><div class="item">Check and record Veltrix security score</div><div class="res"><p class="yn"><i></i>YES<i></i>NO</p><p>Score: ______________</p><p>Top 5 Recommendations:</p><ol class="recs"><li>1.<b></b></li><li>2.<b></b></li><li>3.<b></b></li><li>4.<b></b></li><li>5.<b></b></li></ol><p style="margin-top:5px">Comment:</p><b class="ln"></b></div></div>
    <div class="row"><div class="item">Conditional access Rules (no silly Rules, Geolocation filters in place for Sanctioned Countries)</div><div class="res"><p class="yn"><i></i>YES<i></i>NO</p><p>Comment:</p><b class="ln"></b></div></div>
    <div class="row"><div class="item">Review security access of all privileged access accounts</div><div class="res"><p class="yn"><i></i>YES<i></i>NO</p><p>Comment:</p><b class="ln"></b></div></div>
    <div class="row"><div class="item">Review Application Patching and confirm all workstations are up to date</div><div class="res"><p class="yn"><i></i>YES<i></i>NO</p><p>Comment:</p><b class="ln"></b></div></div>
    <div class="row"><div class="item">Review Velos Patching and confirm all workstations are up to date</div><div class="res"><p class="yn"><i></i>YES<i></i>NO</p><p>Comment:</p><b class="ln"></b></div></div>
    <div class="row"><div class="item">Review domain expiry dates</div><div class="res"><p>Expiry Date: _____/_____/_____</p><p>Comment:</p><b class="ln"></b></div></div>
    <div class="row"><div class="item">Review certificate expiry Dates</div><div class="res"><p>Expiry Date: _____/_____/_____</p><p>Comment:</p><b class="ln"></b></div></div>
    <div class="row"><div class="item">Confirm all devices are in Application Whitelisting enforcement mode</div><div class="res"><p class="yn"><i></i>YES<i></i>NO</p><p>Comment:</p><b class="ln"></b></div></div>
    <div class="row"><div class="item">Ensure DMARC, DKIM and SPF records are in place and up to date</div><div class="res"><p class="yn"><i></i>YES<i></i>NO</p><p>Comment:</p><b class="ln"></b></div></div>
  </div>
  <div class="mark name">CORVELLA SYSTEMS</div><div class="mark tag">SPECIALISED CONSULTING</div>
  <div class="foot-line"></div><div class="foot-url">corvellasystems.qzt.net.au</div><div class="foot-div"></div><div class="foot-num">2</div><div class="foot-bar"></div>
</section>

<!-- Cloud page 3 -->
<section class="page sheet" style="left:789px;top:1161px">
  <svg class="slash" width="50" height="20" aria-hidden="true"><line x1="-2" y1="17" x2="36" y2="-1" stroke="#b5b5b5" stroke-width="4"/></svg>
  <div class="strip-l"></div><div class="strip-r"></div>
  <div class="checklist">
    <div class="row"><div class="item">Confirm Retention Policies are configured and time specified</div><div class="res"><p class="yn"><i></i>YES<i></i>NO</p><p>Comment:</p><b class="ln"></b></div></div>
    <div class="row"><div class="item">Review Network Firewall Firmware is up to date and no ANY &lt;&gt; ANY rules in place</div><div class="res"><p class="yn"><i></i>YES<i></i>NO</p><p>Comment:</p><b class="ln"></b></div></div>
    <div class="row"><div class="item">Ensure critical network equipment is connected to UPS (min 20min run time)</div><div class="res"><p class="yn"><i></i>YES<i></i>NO</p><p>Comment:</p><b class="ln"></b></div></div>
    <div class="row"><div class="item">Ensure Access Layer Network device firmware is up to date (Switches &amp; Access Points)</div><div class="res"><p class="yn"><i></i>YES<i></i>NO</p><p>Comment:</p><b class="ln"></b></div></div>
    <div class="row"><div class="item">Ensure the latest backup configuration for managed network devices is current or automatically backed up monthly. Saved Network location must be secured</div><div class="res"><p class="yn"><i></i>YES<i></i>NO</p><p>Comment:</p><b class="ln"></b></div></div>
    <div class="row"><div class="item">Ensure MFP's &amp; Printers drivers up to date. No Print Nightmare</div><div class="res"><p class="yn"><i></i>YES<i></i>NO</p><p>Comment:</p><b class="ln"></b></div></div>
    <div class="row"><div class="item">NAC Certificates are current (PEAP/EAP-TLS)</div><div class="res"><p class="yn"><i></i>YES<i></i>NO</p><p>Comment:</p><b class="ln"></b></div></div>
    <div class="row"><div class="item">Check DLP alerts and configuration</div><div class="res"><p class="yn"><i></i>YES<i></i>NO</p><p>Comment:</p><b class="ln"></b></div></div>
    <div class="row"><div class="item">Review &amp; address SIEM and SOC alerts</div><div class="res"><p class="yn"><i></i>YES<i></i>NO</p><p>Comment:</p><b class="ln"></b></div></div>
    <div class="row"><div class="item">Email alerting on firewall changes sent to <u style="color:#1d5fc4">alerts@crvl.net.au</u></div><div class="res"><p class="yn"><i></i>YES<i></i>NO</p><p>Comment:</p><b class="ln"></b></div></div>
    <div class="row"><div class="item">Review Vulnerability Scan reports; Remediate as required</div><div class="res"><p class="yn"><i></i>YES<i></i>NO</p><p>Comment:</p><b class="ln"></b></div></div>
    <div class="row"><div class="item">Confirm all Infrastructure is in Monitoring</div><div class="res"><p class="yn"><i></i>YES<i></i>NO</p><p>Comment:</p><b class="ln"></b></div></div>
  </div>
  <div class="mark name">CORVELLA SYSTEMS</div><div class="mark tag">SPECIALISED CONSULTING</div>
  <div class="foot-line"></div><div class="foot-url">corvellasystems.qzt.net.au</div><div class="foot-div"></div><div class="foot-num">3</div><div class="foot-bar"></div>
</section>

<!-- Cloud page 4 -->
<section class="page sheet" style="left:35px;top:1687px">
  <svg class="slash" width="50" height="20" aria-hidden="true"><line x1="-2" y1="17" x2="36" y2="-1" stroke="#b5b5b5" stroke-width="4"/></svg>
  <div class="strip-l"></div><div class="strip-r"></div>
  <div class="checklist" style="top:27px">
    <div class="row"><div class="item">Check vendor Maintenance period of all infrastructure</div><div class="res"><p class="yn"><i></i>YES<i></i>NO</p><p>Comment:</p><b class="ln"></b></div></div>
    <div class="row"><div class="item">Check time sync across all/critical devices</div><div class="res"><p class="yn"><i></i>YES<i></i>NO</p><p>Comment:</p><b class="ln"></b></div></div>
    <div class="row"><div class="item">Check infrastructure firmware</div><div class="res"><p class="yn"><i></i>YES<i></i>NO</p><p>Comment:</p><b class="ln"></b></div></div>
    <div class="row"><div class="item">Review monitoring logs/portal for active alerts</div><div class="res"><p class="yn"><i></i>YES<i></i>NO</p><p>Comment:</p><b class="ln"></b></div></div>
  </div>
  <dl class="sign" style="top:186px"><dt>Completed By</dt><dd>: ______________________________</dd></dl>
  <dl class="sign" style="top:201px"><dt>Signature</dt><dd>: ______________________________</dd></dl>
  <dl class="sign" style="top:216px"><dt>Date</dt><dd>: ______________________________</dd></dl>
  <div class="mark name">CORVELLA SYSTEMS</div><div class="mark tag">SPECIALISED CONSULTING</div>
  <div class="foot-line"></div><div class="foot-url">corvellasystems.qzt.net.au</div><div class="foot-div"></div><div class="foot-num">4</div><div class="foot-bar"></div>
</section>

<!-- Delivery files -->
<div class="delivery-title">Delivery files:</div>
<div class="files">
  <div class="file"><svg width="94" height="115" aria-hidden="true"><path d="M10 3 H62 L91 32 V104 A8 8 0 0 1 83 112 H10 A8 8 0 0 1 2 104 V11 A8 8 0 0 1 10 3 Z M62 3 V32 H91" fill="none" stroke="var(--red)" stroke-width="3.5" stroke-linejoin="round"/></svg><span>PDF</span></div>
  <div class="file"><svg width="94" height="115" aria-hidden="true"><path d="M10 3 H62 L91 32 V104 A8 8 0 0 1 83 112 H10 A8 8 0 0 1 2 104 V11 A8 8 0 0 1 10 3 Z M62 3 V32 H91" fill="none" stroke="var(--dblue)" stroke-width="3.5" stroke-linejoin="round"/></svg><span>WORD</span></div>
  <div class="file"><svg width="94" height="115" aria-hidden="true"><path d="M10 3 H62 L91 32 V104 A8 8 0 0 1 83 112 H10 A8 8 0 0 1 2 104 V11 A8 8 0 0 1 10 3 Z M62 3 V32 H91" fill="none" stroke="var(--green)" stroke-width="3.5" stroke-linejoin="round"/></svg><span>EXCEL</span></div>
  <div class="file"><svg width="94" height="115" aria-hidden="true"><path d="M10 3 H62 L91 32 V104 A8 8 0 0 1 83 112 H10 A8 8 0 0 1 2 104 V11 A8 8 0 0 1 10 3 Z M62 3 V32 H91" fill="none" stroke="var(--orange)" stroke-width="3.5" stroke-linejoin="round"/></svg><span>EPS</span></div>
  <div class="file"><svg width="94" height="115" aria-hidden="true"><path d="M10 3 H62 L91 32 V104 A8 8 0 0 1 83 112 H10 A8 8 0 0 1 2 104 V11 A8 8 0 0 1 10 3 Z M62 3 V32 H91" fill="none" stroke="var(--orange)" stroke-width="3.5" stroke-linejoin="round"/></svg><span>AI</span></div>
</div>

</body>
</html>
```